Sales Flyer Design

Create a Flyer front and back that highlights the different things we do
We do Addition, basements, kitchens, bathrooms, concrete, siding, Roofing.

We want to highlight that we are licensed Electrical Contractor and Plumbers.
Use our Logo attached keeping color scheme mainly our company colors. We are looking for an attention grabbing but easy read for homeowners.

```html
<!DOCTYPE html>
<html lang="en">
<head>
<meta charset="utf-8">
<title>Harlow Remodeling &amp; Restoration – Flyer Front and Back</title>
<link href="https://fonts.googleapis.com/css2?family=Montserrat:wght@400;500;700;800&display=swap" rel="stylesheet">
<style>
  :root{
    --stage:#646464;
    --stage-label:#7a7a7a;
    --orange:#e8552a;
    --orange-deep:#d9481f;
    --black:#0b0b0b;
    --white:#ffffff;
    --ink:#111111;
  }
  *{box-sizing:border-box;margin:0;padding:0}
  html,body{width:1200px;height:835px;overflow:hidden;background:var(--stage)}
  body{position:relative;font-family:"Montserrat",sans-serif}
  .side-label{position:absolute;top:72px;width:503px;text-align:center;font-weight:700;font-size:29px;letter-spacing:1px;color:var(--stage-label)}
  .flyer{position:absolute;top:122px;width:503px;height:650px;background:var(--white);overflow:hidden}
  .flyer--front{left:70px}
  .flyer--back{left:627px}
  .side-label--front{left:70px}
  .side-label--back{left:627px}
  .flyer-art{position:absolute;inset:0;width:100%;height:100%}
  .brand{position:absolute;top:46px;left:0;width:100%;text-align:center;color:var(--white);font-weight:700}
  .brand-name{font-size:30px;letter-spacing:2px;line-height:1}
  .brand-tag{font-size:9.5px;letter-spacing:.6px;margin-top:10px;padding-top:4px;border-top:1px solid rgba(255,255,255,.8);display:inline-block}
  .headline{position:absolute;left:0;width:100%;text-align:center;color:var(--white);line-height:26.5px;font-size:26px}
  .headline .light{font-weight:500;display:block}
  .headline .strong{font-weight:800;display:block}
  .flyer--front .headline{top:328px}
  .flyer--back .headline{top:342px;font-size:25px}
  .intro{position:absolute;left:30px;width:443px;text-align:center;color:var(--white);font-size:8.6px;line-height:11.5px}
  .flyer--front .intro{top:411px}
  .flyer--back .intro{top:425px}
  .services-tab{position:absolute;top:486px;left:161px;width:181px;height:27px;background:var(--white);border-radius:6px;box-shadow:0 2px 4px rgba(0,0,0,.35);text-align:center;line-height:27px;color:var(--orange);font-weight:700;font-size:12px;letter-spacing:1.6px;z-index:2}
  .services{position:absolute;top:506px;left:30px;width:443px;height:79px;background:var(--orange);border-radius:10px}
  .service{position:absolute;color:var(--white);font-size:16px;font-weight:500;display:flex;align-items:center;gap:3px;line-height:1;white-space:nowrap}
  .service svg{width:14px;height:14px;flex:none}
  .services--back .service{font-size:15px}
  .divider{position:absolute;top:14px;height:52px;border-left:1px dotted rgba(255,255,255,.6)}
  .call{position:absolute;top:598px;left:0;width:100%;text-align:center;font-weight:800;font-size:16px;color:var(--ink)}
  .contact{position:absolute;top:620px;left:0;width:100%;text-align:center;font-size:10.5px;font-weight:500;color:var(--ink)}
  .contact .accent{color:var(--orange);font-weight:700}
</style>
</head>
<body>

<div class="side-label side-label--front">FRONT</div>
<div class="side-label side-label--back">BACK</div>

<!-- FRONT -->
<section class="flyer flyer--front">
  <svg class="flyer-art" viewBox="0 0 962 1244" preserveAspectRatio="none">
    <defs>
      <linearGradient id="topFadeFront" x1="0" y1="0" x2="0" y2="1">
        <stop offset="0" stop-color="#e8552a"/>
        <stop offset=".45" stop-color="#e06640"/>
        <stop offset="1" stop-color="#8a7b72"/>
      </linearGradient>
    </defs>
    <g role="img" aria-label="Photo of a remodeled kitchen with white cabinets and a dark island">
      <polygon points="0,8 478,482 0,700" fill="#8f8c88"/>
    </g>
    <g role="img" aria-label="Photo of a finished basement with a stone fireplace and staircase">
      <polygon points="962,8 488,482 962,700" fill="#cfc6b6"/>
    </g>
    <g role="img" aria-label="Faded photo of shingled roofing under the orange header">
      <polygon points="0,0 962,0 483,480" fill="url(#topFadeFront)"/>
    </g>
    <polyline points="0,4 483,482 962,4" fill="none" stroke="#fff" stroke-width="5"/>
    <polygon points="0,698 483,488 962,698 962,712 483,533 0,712" fill="var(--orange)"/>
    <polygon points="0,716 483,543 962,716 962,1101 0,1101" fill="var(--black)"/>
  </svg>

  <div class="brand">
    <div class="brand-name">HARLOW</div>
    <div class="brand-tag">REMODELING &amp; RESTORATION</div>
  </div>

  <h1 class="headline">
    <span class="light">PREMIER</span>
    <span class="strong">LOCAL REMODELING</span>
    <span class="light">COMPANY IN ANKENY, IA</span>
  </h1>

  <p class="intro">We specialize in basements, kitchens, bathrooms, concrete, siding, Roofing.&nbsp; remodeling. You can count on us to work directly with you throughout your entire project to make sure we bring your vision to life. We'll help you choose designs, materials and styles to completely transform the look and feel of your home.</p>

  <div class="services-tab">WE DO ADDITION</div>
  <div class="services services--front">
    <span class="divider" style="left:166px"></span>
    <span class="divider" style="left:305px"></span>
    <div class="service" style="left:37px;top:18px"><svg viewBox="0 0 16 16"><circle cx="8" cy="8" r="6.5" fill="none" stroke="#fff" stroke-width="1.6"/><path d="M5 8.2l2.2 2.2L14 3.5" fill="none" stroke="#fff" stroke-width="1.8"/></svg>Basements</div>
    <div class="service" style="left:37px;top:46px"><svg viewBox="0 0 16 16"><circle cx="8" cy="8" r="6.5" fill="none" stroke="#fff" stroke-width="1.6"/><path d="M5 8.2l2.2 2.2L14 3.5" fill="none" stroke="#fff" stroke-width="1.8"/></svg>Kitchens</div>
    <div class="service" style="left:180px;top:18px"><svg viewBox="0 0 16 16"><circle cx="8" cy="8" r="6.5" fill="none" stroke="#fff" stroke-width="1.6"/><path d="M5 8.2l2.2 2.2L14 3.5" fill="none" stroke="#fff" stroke-width="1.8"/></svg>Bathrooms</div>
    <div class="service" style="left:180px;top:46px"><svg viewBox="0 0 16 16"><circle cx="8" cy="8" r="6.5" fill="none" stroke="#fff" stroke-width="1.6"/><path d="M5 8.2l2.2 2.2L14 3.5" fill="none" stroke="#fff" stroke-width="1.8"/></svg>Concrete</div>
    <div class="service" style="left:322px;top:18px"><svg viewBox="0 0 16 16"><circle cx="8" cy="8" r="6.5" fill="none" stroke="#fff" stroke-width="1.6"/><path d="M5 8.2l2.2 2.2L14 3.5" fill="none" stroke="#fff" stroke-width="1.8"/></svg>Siding</div>
    <div class="service" style="left:322px;top:46px"><svg viewBox="0 0 16 16"><circle cx="8" cy="8" r="6.5" fill="none" stroke="#fff" stroke-width="1.6"/><path d="M5 8.2l2.2 2.2L14 3.5" fill="none" stroke="#fff" stroke-width="1.8"/></svg>Roofing</div>
  </div>

  <p class="call">CALL NOW TODAY! 555-014-2290</p>
  <p class="contact">www.<span class="accent">harlowhomeia</span>.com &nbsp;-&nbsp; info@<span class="accent">harlowhomeia</span>.com</p>
</section>

<!-- BACK -->
<section class="flyer flyer--back">
  <svg class="flyer-art" viewBox="0 0 962 1244" preserveAspectRatio="none">
    <defs>
      <linearGradient id="topFadeBack" x1="0" y1="0" x2="0" y2="1">
        <stop offset="0" stop-color="#e8552a"/>
        <stop offset=".45" stop-color="#df6138"/>
        <stop offset="1" stop-color="#9c5a4a"/>
      </linearGradient>
    </defs>
    <g role="img" aria-label="Photo of an electrician testing wiring in a breaker panel">
      <polygon points="0,8 478,482 0,700" fill="#8a7d70"/>
    </g>
    <g role="img" aria-label="Photo of a plumber fitting a chrome faucet">
      <polygon points="962,8 488,482 962,700" fill="#c9c9cb"/>
    </g>
    <g role="img" aria-label="Faded photo of coloured electrical wires under the orange header">
      <polygon points="0,0 962,0 483,480" fill="url(#topFadeBack)"/>
    </g>
    <polyline points="0,4 483,482 962,4" fill="none" stroke="#fff" stroke-width="5"/>
    <polygon points="0,698 483,488 962,698 962,712 483,533 0,712" fill="var(--orange)"/>
    <polygon points="0,716 483,543 962,716 962,1101 0,1101" fill="var(--black)"/>
  </svg>

  <div class="brand">
    <div class="brand-name">HARLOW</div>
    <div class="brand-tag">REMODELING &amp; RESTORATION</div>
  </div>

  <h1 class="headline">
    <span class="light">PROFESSIONAL</span>
    <span class="strong">ELECTRICAL CONTRACTOR</span>
    <span class="light">AND PLUMBERS.</span>
  </h1>

  <p class="intro">Lorem ipsum dolor sit amet, consectetuer adipiscing elit, sed diam nonummy nibh euismod tincidunt ut laoreet dolore magna aliquam erat volutpat. Ut wisi enim ad minim veniam, quis nostrud exerci tation ullamcorper suscipit lobortis nisl ut aliquip ex ea commodo consequat. Ilum dolore eu feugiat nulla facilisis at vero eros et</p>

  <div class="services-tab">WE DO ADDITION</div>
  <div class="services services--back">
    <span class="divider" style="left:130px"></span>
    <span class="divider" style="left:284px"></span>
    <div class="service" style="left:19px;top:19px"><svg viewBox="0 0 16 16"><circle cx="8" cy="8" r="6.5" fill="none" stroke="#fff" stroke-width="1.6"/><path d="M5 8.2l2.2 2.2L14 3.5" fill="none" stroke="#fff" stroke-width="1.8"/></svg>Installation</div>
    <div class="service" style="left:19px;top:45px"><svg viewBox="0 0 16 16"><circle cx="8" cy="8" r="6.5" fill="none" stroke="#fff" stroke-width="1.6"/><path d="M5 8.2l2.2 2.2L14 3.5" fill="none" stroke="#fff" stroke-width="1.8"/></svg>Lighting</div>
    <div class="service" style="left:138px;top:19px"><svg viewBox="0 0 16 16"><circle cx="8" cy="8" r="6.5" fill="none" stroke="#fff" stroke-width="1.6"/><path d="M5 8.2l2.2 2.2L14 3.5" fill="none" stroke="#fff" stroke-width="1.8"/></svg>Celling Fans</div>
    <div class="service" style="left:138px;top:45px"><svg viewBox="0 0 16 16"><circle cx="8" cy="8" r="6.5" fill="none" stroke="#fff" stroke-width="1.6"/><path d="M5 8.2l2.2 2.2L14 3.5" fill="none" stroke="#fff" stroke-width="1.8"/></svg>LED Conversion</div>
    <div class="service" style="left:291px;top:19px"><svg viewBox="0 0 16 16"><circle cx="8" cy="8" r="6.5" fill="none" stroke="#fff" stroke-width="1.6"/><path d="M5 8.2l2.2 2.2L14 3.5" fill="none" stroke="#fff" stroke-width="1.8"/></svg>Panel Upgrade</div>
    <div class="service" style="left:291px;top:45px"><svg viewBox="0 0 16 16"><circle cx="8" cy="8" r="6.5" fill="none" stroke="#fff" stroke-width="1.6"/><path d="M5 8.2l2.2 2.2L14 3.5" fill="none" stroke="#fff" stroke-width="1.8"/></svg>Switches</div>
  </div>

  <p class="call">CALL NOW TODAY! 555-014-2290</p>
  <p class="contact">www.<span class="accent">harlowhomeia</span>.com &nbsp;-&nbsp; info@<span class="accent">harlowhomeia</span>.com</p>
</section>

</body>
</html>
```